Business Card

We are looking to re-create our business card. Attached is the company logo. we would like it to be back and front. for example one side with the persons information and the other side with the company logo. Be as creative as you would like but also keep in mind, we are a Health Insurance company and we need to look professional as well.
Industry/Entity Type
Business

```html
<!DOCTYPE html>
<html lang="en">
<head>
<meta charset="utf-8">
<title>Harbor Wellness Group — Business Card</title>
<link href="https://fonts.googleapis.com/css2?family=Open+Sans:wght@400;700&display=swap" rel="stylesheet">
<style>
  :root {
    --backdrop: #d5e9e1;
    --card-white: #ffffff;
    --brand-blue: #0a8fd6;
    --brand-blue-deep: #0070bd;
    --edge-navy: #0d3553;
    --text-grey: #8c8c8c;
    --logo-grey: #8a8a8a;
    --name-blue: #1a8fd1;
  }
  html, body {
    margin: 0;
    width: 1200px;
    height: 856px;
    overflow: hidden;
    background: var(--backdrop);
    font-family: "Open Sans", Arial, sans-serif;
  }
  .canvas {
    position: relative;
    width: 1200px;
    height: 856px;
  }
  .card {
    position: absolute;
    top: 285px;
    width: 500px;
    height: 286px;
    border-radius: 28px;
    overflow: hidden;
    background: var(--card-white);
    box-shadow: 0 10px 24px rgba(30, 70, 60, 0.18);
  }
  .card--front { left: 70px; }
  .card--back { left: 630px; }
  .card-art {
    position: absolute;
    inset: 0;
    width: 500px;
    height: 286px;
  }
  .brand-mark {
    position: absolute;
    left: 40px;
    top: 112px;
    font-size: 28px;
    font-weight: 700;
    color: var(--logo-grey);
    letter-spacing: -1px;
  }
  .brand-divider {
    position: absolute;
    left: 112px;
    top: 100px;
    width: 1px;
    height: 54px;
    background: var(--logo-grey);
  }
  .company-name {
    position: absolute;
    left: 124px;
    top: 98px;
    font-size: 20px;
    font-weight: 700;
    color: var(--name-blue);
    margin: 0;
  }
  .contact {
    position: absolute;
    margin: 0;
    font-size: 16px;
    line-height: 23px;
    color: var(--text-grey);
    font-style: normal;
  }
  .contact--front {
    right: 150px;
    top: 146px;
    text-align: right;
  }
  .contact--back {
    left: 0;
    right: 0;
    top: 104px;
    text-align: center;
    font-size: 15px;
    line-height: 22px;
  }
</style>
</head>
<body>
<main class="canvas">

  <section class="card card--front" aria-label="Card front">
    <svg class="card-art" viewBox="0 0 500 286" aria-hidden="true">
      <defs>
        <linearGradient id="blueBand" x1="0" y1="0" x2="1" y2="1">
          <stop offset="0" stop-color="#0a8fd6"/>
          <stop offset="1" stop-color="#0070bd"/>
        </linearGradient>
      </defs>
      <rect width="500" height="286" fill="url(#blueBand)"/>
      <path d="M0,0 H464 C526,96 504,244 332,264 C226,276 144,246 102,208 L0,222 Z" fill="var(--edge-navy)"/>
      <path d="M0,0 H452 C512,90 492,232 330,254 C230,266 150,238 110,202 L0,216 Z" fill="var(--card-white)"/>
    </svg>
    <div class="brand-mark">HWG</div>
    <div class="brand-divider"></div>
    <h1 class="company-name">Harbor Wellness Group</h1>
    <address class="contact contact--front">
      Nadia@harborwellness.com<br>
      000 - 1XXXXX xx<br>
      000 - XXXx - XXX
    </address>
  </section>

  <section class="card card--back" aria-label="Card back">
    <svg class="card-art" viewBox="0 0 500 286" aria-hidden="true">
      <path d="M0,0 H140 C70,30 30,110 24,286 H0 Z" fill="var(--brand-blue-deep)"/>
      <path d="M0,0 H130 C66,32 30,110 16,286 H0 Z" fill="var(--brand-blue)"/>
      <path d="M300,0 H500 V170 C488,90 420,24 300,0 Z" fill="var(--edge-navy)"/>
      <path d="M310,0 H500 V150 C486,80 420,22 310,0 Z" fill="var(--brand-blue)"/>
    </svg>
    <address class="contact contact--back">
      Nadia@harborwellness.com<br>
      000 - 1XXXXX xx<br>
      000 - XXXx - XXX
    </address>
  </section>

</main>
</body>
</html>
```